Book Cover Design — Literary Memoir — Seven Winters Beneath a Borrowed Moon

I need a professional book cover design for a literary memoir titled Seven Winters Beneath a Borrowed Moon by Dorota K. Whitfield. This project requires two complete cover files — one for the paperback edition and one for the hardcover edition — both built to Printvane print specifications.
The author photograph is attached and is the centerpiece of the front cover. It is not a placeholder. The front cover contains three elements only: the author name, the photograph, and the title. No subtitle, no taglines, no additional elements.
A complete creative brief is attached. Read it in full before submitting a design. It contains all specifications, typography direction, mood references, comparable covers, and file delivery requirements.
A back cover text package is also attached for layout reference. A Canva reference design showing the directional concept is attached — the photograph placement and title position are correct. The typography needs professional resolution.
This is a literary memoir in the tradition of Unlearned, Cartography, and The Paper Orchard. The cover must feel sophisticated, restrained, and literary — not self-help, not inspirational, not decorative.
Two formats required. Paperback and hardcover. Printvane spine templates for both formats are attached.
Full file delivery specifications are in the brief. The color photograph in front of the water in the blue jacket should be used inside the dust jacket with the bio if a dust jacket edition is produced.
Do not use literal interpretations of the title. No whiskey glasses, no alcohol, no angel figurines, no cherubs, no wings, no halos, no religious imagery of any kind. The title is metaphorical. The cover must not illustrate it literally.
The author photograph is the only image on the front cover. Typography, photograph, author name. Nothing else.

BRIEF UPDATE — BACK COVER PHOTOGRAPH AND LAYOUT
Please read before submitting.
A second author photograph is attached to this brief. It is a color photograph and it is specifically for the back cover author bio section only. Do not convert it to black and white. Do not use it on the front cover. The front cover uses only the black and white photograph already provided. The color photograph is for the back cover exclusively. Do not generate, substitute, or alter the image. Use only the file provided.
Back cover layout — exact order top to bottom:
1. Endorsement quotes — top of back cover.
Three endorsement quote placeholders, each approximately two to three lines of quote text followed by the endorser name and credential on the line below. Separate each quote with a thin rule or line. Set in italics, smaller than the jacket copy text. These are placeholders — final quotes are pending.
2. Jacket copy — middle of back cover.
The main descriptive text block. Set in a clean readable serif, slightly larger than the endorsement quotes. Preserve all paragraph breaks exactly as written. Two pull quotes inside the jacket copy must be set in gold, framed by thin gold rules above and below, matching the gold accent color used for BORROWED MOON on the front cover. Use the following final approved text exactly as written:
At forty-three, she stood in a villa in Abu Dhabi at four in the morning and understood that the marriage was over, the career she had given up was not coming back, and the country she was standing in was not hers. She had two boys to raise, a spousal visa, and no plan.
She came by the next move honestly.
A great-grandmother who crossed the Atlantic alone in 1907 and built a life from nothing. A grandmother on the other side, told by an anonymous letter that the blood in her veins was tainted, who answered the letter with the rest of her life. A guardian angel with a slightly crooked halo and a highball in her hand. Four generations of women who refused the smaller life and passed something down that none of them named and none of them had to.
Seven Winters Beneath a Borrowed Moon is the story of what happens when a woman finally stops building someone else's life and starts building her own.
[GOLD PULL QUOTE — framed by thin gold rules above and below, set in gold, centered:]
For anyone who has ever had no choice but to start over — and for anyone still waiting for the courage to.
[End gold pull quote]
Proof that someone has navigated it.
And that you can too.
The closing two lines — Proof that someone has navigated it. and And that you can too. — should each sit on their own line with breathing room around them. They are the closing beats of the back cover.
3. Author bio with photograph — bottom of back cover.
Place the color author photograph on the left side, cropped to approximately a two inch square or whatever proportion fits the layout cleanly. The author bio text runs to the right of the photograph. The author name DOROTA K. WHITFIELD should appear above the bio text in gold caps. Use the following text exactly as written, with one paragraph break inserted between finally behind her. and When the marriage ended:
Dorota K. Whitfield is the founder and CEO of Tallowmere Advisory, an international advisory firm operating across the United States, the Middle East, Africa, and Europe. She gave up a rising career in Pennsylvania state government to support her husband, an KR-19T Osprite pilot, through five combat deployments. She followed him to Abu Dhabi in 2013 believing the hardest years were finally behind her.
When the marriage ended, she was forty-three, in a country that was not hers, with no job and no road back. She rebuilt from nothing and went on to advise governments, ministries, Vantage 400 companies, and members of the Royal Family of Abu Dhabi. She has spoken on stages in over thirty countries. She lives in North Carolina.
4. Barcode and ISBN — lower right corner.
Minimum clear space 2 inches wide by 1.2 inches tall. No other design elements within 0.25 inches of the barcode block.
Background treatment:
The back cover background should not be flat black. Add a subtle texture, very light gradient, or carry a soft element from the front cover photograph into the background to give the back cover visual depth and weight. It should feel finished and intentional, not like an empty void with text dropped onto it.
Typography:
Consistent with the front cover type treatment. Same font family throughout. Endorsement quotes in italics. Jacket copy in roman. Author bio in roman at slightly smaller size than the jacket copy. The gold pull quote inside the jacket copy is set in gold, centered, framed by thin gold rules above and below. The author name above the bio is set in gold caps. All other text is white or very light grey, fully legible against the dark background.
Do not add anything else to the back cover. No additional images, no decorative elements, no additional text beyond what is specified above.

Target Market(s)

Women aged 35 to 65. Readers of literary memoir and narrative nonfiction. Military spouse community. Women navigating reinvention, divorce, or major life transition. Business and leadership audience. Book club readers. Comparable readership to Unlearned by Mira Lockhaven, Cartography by Joss Verhulst, and The Paper Orchard by Corinne Dabney.

Industry/Entity Type

Industry: Book publishing. Literary memoir. Narrative nonfiction.

Font styles to use
Serif
Sans Serif
Other font styles liked:
• Garamond, Caslon, or Freight Display. Clean geometric sans-serif such as Futura or Gotham. Avoid fonts that read as corporate, casual, or decorative. The font chosen for the title must work in both white and gold without losing legibility against the dark photographic background.

Requirements
Must have
• The author photograph — black and white, attached, full bleed, centerpiece of the cover. This is not a placeholder. Do not alter, colorize, or filter it. Author name: DOROTA K. WHITFIELD — top of cover, white, clean and strong. Title: SEVEN WINTERS BENEATH A BORROWED MOON — lower third of cover. BORROWED MOON in gold. All other title words in white. Unified typography — all words of the title must feel like one visual system. This is the primary design challenge. Two complete cover files — one paperback, one hardcover — built to the attached Printvane spine templates. Print-ready PDF both formats, editable source files both formats, front cover flat image for ebook, square audiobook cover 2400 x 2400 pixels.
Nice to have
• A drop cap treatment on the I that opens the title, if the designer can make it feel intentional and unified with the rest of the title rather than decorative. Back cover placeholder showing the design treatment and barcode placement area — full back cover text is provided in the attached back cover package for layout sizing. Subtle gold accent elements if they enhance rather than decorate — the gold should feel intentional, not ornamental.
Should not have
• No subtitle. No tagline. No credential lines. No award badges. No endorsement quotes on the front cover. No brushstroke fonts. No handwritten fonts. No decorative display fonts. No more than two typeface families in the entire design. No additional colors beyond white, gold, and the black and white photograph. No colorizing, filtering, or altering the photograph in any way. No graphic elements, borders, frames, or decorative embellishments. No busy or cluttered layout — negative space is the design language of this cover. Nothing that reads as self-help, inspirational poster, or business book. Do not use literal interpretations of the title. No whiskey glasses, no alcohol, no angel figurines, no cherubs, no wings, no halos, no religious imagery of any kind. The title is metaphorical. The cover must not illustrate it literally. The author photograph is the only image on the front cover. Typography, photograph, author name. Nothing else.

```html
<!DOCTYPE html>
<html lang="en">
<head>
<meta charset="utf-8">
<title>Seven Winters Beneath a Borrowed Moon — Cover Wrap</title>
<link rel="stylesheet" href="https://fonts.googleapis.com/css2?family=EB+Garamond:ital,wght@0,400;0,500;0,600;1,400&family=Montserrat:wght@700;800;900&display=swap">
<style>
  :root {
    --stage: #d9d9d9;
    --ink: #0b0b0b;
    --spine: #1a1a1a;
    --white: #ffffff;
    --light: #e8e8e8;
    --muted: #c4c4c4;
    --gold-light: #f3dfa3;
    --gold: #c9a04a;
    --gold-deep: #8a6a26;
    --barcode-area: #a8a8a8;
  }
  * { box-sizing: border-box; margin: 0; padding: 0; }
  html, body { width: 1200px; height: 960px; overflow: hidden; }
  body {
    background: var(--stage);
    font-family: "EB Garamond", serif;
    color: var(--light);
  }
  .cover-wrap {
    position: absolute;
    left: 132px; top: 150px;
    width: 936px; height: 660px;
    display: flex;
    box-shadow: 0 18px 40px rgba(0,0,0,.25);
  }

  /* Back cover */
  .back-cover {
    width: 440px; height: 100%;
    background:
      radial-gradient(ellipse at 88% 8%, #2a2a2a 0%, rgba(42,42,42,0) 55%),
      radial-gradient(ellipse at 10% 95%, #1d1d1d 0%, rgba(29,29,29,0) 50%),
      linear-gradient(180deg, #121212 0%, var(--ink) 60%, #131313 100%);
    padding: 22px 32px 20px;
    display: flex;
    flex-direction: column;
  }
  .endorsement { padding: 0 0 5px; }
  .endorsement + .endorsement { border-top: 0.5px solid rgba(255,255,255,.22); padding-top: 5px; }
  .endorsement-quote {
    font-style: italic;
    font-size: 8.4px;
    line-height: 1.3;
    color: var(--muted);
  }
  .endorsement-credit {
    font-size: 8px;
    text-align: right;
    color: var(--white);
    margin-top: 1px;
  }
  .gold-rule {
    width: 110px; height: 1.2px;
    background: linear-gradient(90deg, var(--gold-deep), var(--gold-light), var(--gold));
    margin: 6px auto 8px;
  }
  .jacket-copy p {
    font-size: 9.6px;
    line-height: 1.3;
    color: var(--white);
    margin-bottom: 4px;
  }
  .pull-quote {
    margin: 6px 30px;
    padding: 5px 0;
    border-top: 0.8px solid var(--gold);
    border-bottom: 0.8px solid var(--gold);
    text-align: center;
    font-style: italic;
    font-size: 10px;
    line-height: 1.3;
    color: var(--gold);
  }
  .jacket-copy .closing {
    text-align: center;
    font-size: 10px;
    margin: 0;
  }
  .jacket-copy .closing:first-of-type { margin-top: 4px; }
  .closing-block { margin: 5px 0 2px; }
  .author-bio {
    display: flex;
    gap: 11px;
    align-items: flex-start;
    margin-top: 4px;
  }
  .bio-photo {
    flex: 0 0 80px; height: 80px;
    background: linear-gradient(160deg, #5b6f86 0%, #2f3f55 60%, #22303f 100%);
  }
  .bio-name {
    font-family: "EB Garamond", serif;
    font-weight: 600;
    font-size: 9px;
    letter-spacing: 1px;
    color: var(--gold);
    margin-bottom: 2px;
  }
  .bio-text p { font-size: 7.9px; line-height: 1.25; color: var(--light); }
  .bio-text p + p { margin-top: 2px; }
  .barcode-area {
    margin-top: auto;
    align-self: flex-end;
    width: 112px; height: 62px;
    background: var(--barcode-area);
  }

  /* Spine */
  .spine {
    width: 56px; height: 100%;
    background: linear-gradient(90deg, #111 0%, var(--spine) 35%, #2a2a2a 50%, var(--spine) 65%, #111 100%);
    display: flex;
    flex-direction: column;
    justify-content: space-between;
    align-items: center;
    padding: 34px 0 26px;
  }
  .spine-title, .spine-author {
    writing-mode: vertical-rl;
    font-family: "Montserrat", sans-serif;
    color: var(--white);
    text-transform: uppercase;
  }
  .spine-title { font-weight: 800; font-size: 17px; letter-spacing: .3px; }
  .spine-author { font-weight: 800; font-size: 9.5px; line-height: 1.1; }

  /* Front cover */
  .front-cover {
    width: 440px; height: 100%;
    position: relative;
    overflow: hidden;
    background: var(--ink);
  }
  .front-photo {
    position: absolute; inset: 0;
    background:
      radial-gradient(ellipse 55% 45% at 88% 28%, #8d8d8d 0%, #4a4a4a 45%, rgba(40,40,40,0) 75%),
      radial-gradient(ellipse 40% 35% at 95% 58%, #6e6e6e 0%, rgba(50,50,50,0) 70%),
      linear-gradient(180deg, #1b1b1b 0%, #3a3a3a 45%, #151515 80%, #0a0a0a 100%);
  }
  .front-author {
    position: absolute;
    top: 48px; left: 0; right: 0;
    text-align: center;
    font-family: "Montserrat", sans-serif;
    font-weight: 800;
    font-size: 19px;
    color: var(--white);
    letter-spacing: .3px;
  }
  .front-title {
    position: absolute;
    left: 36px; bottom: 58px;
    font-family: "Montserrat", sans-serif;
    font-weight: 900;
    font-size: 30px;
    line-height: 1.22;
    color: var(--white);
    text-transform: uppercase;
  }
  .front-title .accent {
    background: linear-gradient(180deg, var(--gold-light) 0%, var(--gold) 50%, var(--gold-deep) 100%);
    -webkit-background-clip: text;
    background-clip: text;
    color: transparent;
  }
</style>
</head>
<body>
  <main class="cover-wrap">
    <section class="back-cover">
      <div class="endorsements">
        <div class="endorsement">
          <p class="endorsement-quote">Lorem ipsum dolor sit amet, consectetur adipiscing elit, sed do eiusmod tempor incididunt ut labore et dolore magna aliqua. Quis ipsum suspendisse ultrices gravida. Risus commodo viverra maecenas accumsan lacus vel facilisis.</p>
          <p class="endorsement-credit">Endorser Name, Title or Credential</p>
        </div>
        <div class="endorsement">
          <p class="endorsement-quote">Lorem ipsum dolor sit amet, consectetur adipiscing elit, sed do eiusmod tempor incididunt ut labore et dolore magna aliqua. Quis ipsum suspendisse ultrices gravida. Risus commodo viverra maecenas accumsan lacus vel facilisis.</p>
          <p class="endorsement-credit">Endorser Name, Title or Credential</p>
        </div>
        <div class="endorsement">
          <p class="endorsement-quote">Lorem ipsum dolor sit amet, consectetur adipiscing elit, sed do eiusmod tempor incididunt ut labore et dolore magna aliqua. Quis ipsum suspendisse ultrices gravida. Risus commodo viverra maecenas accumsan lacus vel facilisis.</p>
          <p class="endorsement-credit">Endorser Name, Title or Credential</p>
        </div>
      </div>

      <div class="gold-rule"></div>

      <div class="jacket-copy">
        <p>At forty-three, she stood in a villa in Abu Dhabi at four in the morning and understood that the marriage was over, the career she had given up was not coming back, and the country she was standing in was not hers. She had two boys to raise, a spousal visa, and no plan.</p>
        <p>She came by the next move honestly.</p>
        <p>A great-grandmother who crossed the Atlantic alone in 1907 and built a life from nothing. A grandmother on the other side, told by an anonymous letter that the blood in her veins was tainted, who answered the letter with the rest of her life. A guardian angel with a slightly crooked halo and a highball in her hand. Four generations of women who refused the smaller life and passed something down that none of them named and none of them had to.</p>
        <p>Seven Winters Beneath a Borrowed Moon is the story of what happens when a woman finally stops building someone else's life and starts building her own.</p>
        <p class="pull-quote">For anyone who has ever had no choice but to start over — and for anyone still waiting for the courage to.</p>
        <div class="closing-block">
          <p class="closing">Proof that someone has navigated it.</p>
          <p class="closing">And that you can too.</p>
        </div>
      </div>

      <div class="gold-rule"></div>

      <div class="author-bio">
        <div class="bio-photo" role="img" aria-label="Colour portrait of the author in a blue jacket in front of water"></div>
        <div class="bio-text">
          <h2 class="bio-name">DOROTA K. WHITFIELD</h2>
          <p>Dorota K. Whitfield is the founder and CEO of Tallowmere Advisory, an international advisory firm operating across the United States, the Middle East, Africa, and Europe. She gave up a rising career in Pennsylvania state government to support her husband, an KR-19T Osprite pilot, through five combat deployments. She followed him to Abu Dhabi in 2013 believing the hardest years were finally behind her.</p>
          <p>When the marriage ended, she was forty-three, in a country that was not hers, with no job and no road back. She rebuilt from nothing and went on to advise governments, ministries, Vantage 400 companies, and members of the Royal Family of Abu Dhabi. She has spoken on stages in over thirty countries. She lives in North Carolina.</p>
        </div>
      </div>

      <div class="barcode-area" aria-label="Barcode and ISBN area"></div>
    </section>

    <section class="spine">
      <span class="spine-title">Seven Winters Beneath a Borrowed Moon</span>
      <span class="spine-author">Dorota K.<br>Whitfield</span>
    </section>

    <section class="front-cover">
      <div class="front-photo" role="img" aria-label="Black and white author portrait, face at the right edge against a dark studio background"></div>
      <p class="front-author">DOROTA K. WHITFIELD</p>
      <h1 class="front-title">Seven Winters<br>Beneath a<br><span class="accent">Borrowed Moon</span></h1>
    </section>
  </main>
</body>
</html>
```